Helix Anchor Works Website

Hello we are a screw piling business based in Sydney.
Screw piling is basically drilling steel into the ground with a excavator.

The website needs to have similar information as http://www.brightgroundworks.com.au/. It is basically the same business.

The business name is Helix Anchor Works.

Logo is attached.

Website needs to be wordpress ready.
With SEO.
Want to be able to edit in wordpress.

Target Market(s)

Business to Business and Normal

Industry/Entity Type

Construction

Coding

Coded - Design and coding required

Number of Pages Required

5+ page

Font styles to use
Serif
Sans Serif
Decorative

Requirements
Nice to have
• Information about screw piering.

```html
<!DOCTYPE html>
<html lang="en">
<head>
<meta charset="utf-8">
<title>Helix Anchor Works</title>
<link href="https://fonts.googleapis.com/css2?family=Questrial&family=Open+Sans:ital,wght@0,400;0,600;1,400&display=swap" rel="stylesheet">
<style>
:root{
  --blue:#0a64d8;
  --blue-bright:#1f7cf0;
  --ink:#1d1d1d;
  --black:#0a0a0a;
  --grey-bg:#ececec;
  --text:#555;
  --white:#fff;
}
*{margin:0;padding:0;box-sizing:border-box}
html,body{width:723px;height:1200px;overflow:hidden;background:var(--white)}
body{position:relative;font-family:"Open Sans",sans-serif;color:var(--ink)}
h1,h2,h3{font-weight:400}
.abs{position:absolute}

/* header */
.site-header{left:0;top:0;width:723px;height:56px;background:var(--white);border-bottom:1px solid #ddd}
.brand{left:32px;top:15px;font-family:"Questrial",sans-serif;font-size:17px;color:var(--blue);letter-spacing:.5px;display:flex;align-items:center;gap:7px}
.brand-mark{width:12px;height:12px;background:var(--blue)}
.nav{left:0;top:0;height:56px}
.nav a{position:absolute;top:0;height:56px;line-height:60px;font-size:7px;color:var(--blue);text-decoration:none;white-space:nowrap}
.nav a.active{background:var(--blue);color:var(--white);width:34px;text-align:center}
.call{left:588px;top:15px;display:flex;gap:5px;align-items:center}
.call-label{font-size:7px;color:var(--blue);line-height:1}
.call-number{font-size:11px;color:#666;line-height:1.2}

/* hero */
.hero{left:0;top:56px;width:723px;height:376px;overflow:hidden}
.hero-photo{left:0;top:0;width:723px;height:376px;background:linear-gradient(180deg,#6d8fa6 0%,#5f88a6 45%,#4d7799 100%)}
.hero-title{right:31px;top:112px;text-align:right;font-family:"Questrial",sans-serif;font-size:28px;line-height:33px;color:var(--white);letter-spacing:.5px}
.hero-text{right:31px;top:188px;width:300px;text-align:right;font-family:"Questrial",sans-serif;font-size:8.6px;line-height:13.6px;color:var(--white)}
.hero-btn{left:628px;top:236px;width:68px;height:20px;background:var(--white);color:var(--blue);font-family:"Questrial",sans-serif;font-size:8.5px;line-height:20px;text-align:center}
.dots{left:616px;top:325px;display:flex;gap:5px}
.dots span{width:14px;height:2px;background:#111}
.dots span.on{background:var(--white)}

/* services band */
.services{left:0;top:432px;width:723px;height:128px;background:var(--black);border-top:2px solid var(--white)}
.service{top:0;width:150px;height:128px;text-align:center}
.service-icon{position:absolute;left:50%;top:-22px;margin-left:-25px;width:50px;height:50px;border-radius:50%;background:var(--blue);border:3px solid var(--white);display:flex;align-items:center;justify-content:center}
.service-icon.light{background:var(--white);border-color:var(--blue)}
.service-title{position:absolute;top:40px;width:100%;font-family:"Questrial",sans-serif;font-size:10px;color:var(--blue-bright)}
.service-text{position:absolute;top:56px;width:100%;font-size:7px;line-height:10.3px;color:var(--white)}
.service-btn{position:absolute;top:94px;left:50%;margin-left:-22px;width:44px;height:16px;border:1px solid var(--blue);color:var(--white);font-size:7px;line-height:14px}
.service-btn.filled{background:var(--blue)}
.band-arrow{top:484px}

/* welcome */
.welcome-title{left:0;top:584px;width:723px;text-align:center;font-family:"Questrial",sans-serif;font-size:21px;color:var(--ink)}
.welcome-title span{color:var(--blue)}
.welcome-text{left:70px;top:621px;width:583px;text-align:center;font-size:7px;line-height:13.6px;color:var(--text)}
.welcome-btn{left:326px;top:665px;width:69px;height:23px;background:var(--blue);color:var(--white);font-size:7px;line-height:23px;text-align:center}

/* testimonial */
.testimonials{left:0;top:720px;width:723px;height:199px;background:var(--grey-bg)}
.quote-box{left:207px;top:763px;width:240px;height:102px;background:var(--white)}
.quote-text{left:220px;top:789px;width:215px;font-size:7px;line-height:13.6px;font-style:italic;color:#9a9a9a}
.quote-mark{left:202px;top:756px}
.avatar{left:475px;top:767px;width:44px;height:44px;border-radius:50%;background:linear-gradient(#d9c2ad,#8d7765);border:2px solid var(--white)}
.person{left:474px;top:818px;font-family:"Questrial",sans-serif;font-size:11px;color:var(--blue)}
.person-loc{left:474px;top:834px;font-size:7px;color:#888}

/* footer */
.footer{left:0;top:919px;width:723px;height:234px;background:linear-gradient(180deg,#121212,#0c0c0c)}
.footer-h{font-family:"Questrial",sans-serif;font-size:18px;color:var(--blue-bright);font-weight:700}
.contact-h{right:415px;top:963px;text-align:right}
.contact-lines{right:415px;top:997px;text-align:right;font-family:"Questrial",sans-serif;font-size:11px;line-height:17px;color:var(--white)}
.social{left:233px;top:1077px;display:flex;gap:6px}
.social span{width:20px;height:20px;border-radius:50%;border:1px solid #ccc}
.social span.on{background:var(--blue);border-color:var(--white)}
.divider{left:348px;top:964px;width:1px;height:152px;background:#333}
.news-h{left:386px;top:963px}
.news-text{left:388px;top:997px;width:210px;font-size:7.5px;line-height:14px;color:var(--white)}
.email{left:390px;top:1033px;width:198px;height:26px;border:1px solid #333;font-size:7.5px;color:#888;line-height:24px;padding-left:13px}
.subscribe{left:390px;top:1073px;width:198px;height:26px;background:var(--blue);color:var(--white);font-size:7.5px;line-height:26px;text-align:center}

.bottom-bar{left:0;top:1153px;width:723px;height:47px;background:var(--blue)}
.legal{left:30px;top:1175px;font-size:6px;color:var(--white)}
.copyright{right:29px;top:1173px;font-size:6px;color:var(--white)}
</style>
</head>
<body>

<header class="site-header abs">
  <div class="brand abs"><span class="brand-mark"></span>Helix Anchor Works</div>
  <nav class="nav abs">
    <a class="active" style="left:221px">HOME</a>
    <a style="left:277px">ABOUT US</a>
    <a style="left:340px">PRODUCTS</a>
    <a style="left:404px">BENEFITS</a>
    <a style="left:464px">FAQ</a>
    <a style="left:505px">CONTACT US</a>
  </nav>
  <div class="call abs">
    <svg width="22" height="22" viewBox="0 0 22 22"><circle cx="11" cy="11" r="10" fill="none" stroke="#0a64d8" stroke-width="1.2"/><path d="M7.5 6.5c.6-.6 1.3-.4 1.6.2l.8 1.5c.3.5 0 1-.4 1.3l-.5.4c.5 1.2 1.4 2.2 2.6 2.7l.4-.5c.3-.4.8-.6 1.3-.3l1.5.8c.6.3.7 1 .2 1.6-.9 1-2.4 1.1-3.7.3-1.9-1.1-3.2-2.6-4-4.4-.5-1.3-.3-2.7.2-3.6z" fill="#0a64d8"/></svg>
    <div><div class="call-label">Call Us</div><div class="call-number">0400-555-218</div></div>
  </div>
</header>

<section class="hero abs">
  <div class="hero-photo abs" role="img" aria-label="Photo of pelicans resting on old timber piles in calm blue water"></div>
  <svg class="abs" style="left:0;top:0" width="723" height="376" viewBox="0 0 723 376"><polygon points="405,0 723,0 723,376 277,376" fill="#0a64d8" opacity=".85"/></svg>
  <h1 class="hero-title abs">ANOTHER IDEAL SCREW<br>PILE INSTALLATION</h1>
  <p class="hero-text abs">Lorem ipsum dolor sit amet, consectetur adipiscing elit, sed do eiusmod tempor incididunt ut labore et dolore magna aliqua. Ut enim ad minim veniam, quis nostrud exercitation ullamco laboris</p>
  <div class="hero-btn abs">Read More</div>
  <div class="dots abs"><span></span><span class="on"></span><span></span></div>
</section>

<section class="services abs">
  <div class="service abs" style="left:29px">
    <div class="service-icon light"><svg width="20" height="16" viewBox="0 0 20 16" fill="#0a64d8"><circle cx="10" cy="4" r="3"/><circle cx="4" cy="5" r="2.3"/><circle cx="16" cy="5" r="2.3"/><path d="M5 15c0-4 2.2-6 5-6s5 2 5 6z"/><path d="M0 14c0-3 1.6-5 4-5 1 0 1.6.3 2 .7-1 1.2-1.6 2.6-1.7 4.3z"/><path d="M20 14c0-3-1.6-5-4-5-1 0-1.6.3-2 .7 1 1.2 1.6 2.6 1.7 4.3z"/></svg></div>
    <div class="service-title">Anchorline Domestic</div>
    <div class="service-text">Lorem ipsum dolor sit amet, consecte-<br>tur ipsum dolor sit amet, consectetur<br>adipis do edit at labour</div>
    <div class="service-btn filled">MORE ▸</div>
  </div>
  <div class="service abs" style="left:197px">
    <div class="service-icon"><svg width="20" height="20" viewBox="0 0 20 20"><circle cx="10" cy="10" r="8" fill="none" stroke="#fff" stroke-width="3"/><circle cx="10" cy="10" r="3.5" fill="none" stroke="#fff" stroke-width="1.5"/></svg></div>
    <div class="service-title">Anchorline Commercial</div>
    <div class="service-text">Lorem ipsum dolor sit amet, consecte-<br>tur ipsum dolor sit amet, consectetur<br>adipis do edit at labour</div>
    <div class="service-btn">MORE ▸</div>
  </div>
  <div class="service abs" style="left:365px">
    <div class="service-icon"><svg width="22" height="20" viewBox="0 0 22 20" fill="none" stroke="#fff" stroke-width="1.6"><rect x="7" y="2" width="8" height="7"/><rect x="2" y="11" width="8" height="7"/><rect x="12" y="11" width="8" height="7"/></svg></div>
    <div class="service-title">Anchorline Demountable</div>
    <div class="service-text">Lorem ipsum dolor sit amet, consecte-<br>tur ipsum dolor sit amet, consectetur<br>adipis do edit at labour</div>
    <div class="service-btn">MORE ▸</div>
  </div>
  <div class="service abs" style="left:540px">
    <div class="service-icon"><svg width="20" height="18" viewBox="0 0 20 18" fill="#fff"><rect x="2" y="2" width="7" height="5"/><rect x="11" y="2" width="7" height="5"/><rect x="2" y="9" width="7" height="5"/><rect x="11" y="9" width="7" height="5"/></svg></div>
    <div class="service-title">Advantages of Screw Piles</div>
    <div class="service-text">Lorem ipsum dolor sit amet, consecte-<br>tur ipsum dolor sit amet, consectetur<br>adipis do edit at labour</div>
    <div class="service-btn">MORE ▸</div>
  </div>
</section>
<svg class="band-arrow abs" style="left:13px" width="12" height="14" viewBox="0 0 12 14"><polygon points="11,0 11,14 0,7" fill="#fff"/></svg>
<svg class="band-arrow abs" style="left:699px" width="12" height="14" viewBox="0 0 12 14"><polygon points="1,0 1,14 12,7" fill="#fff"/></svg>

<section>
  <h2 class="welcome-title abs">Welcome to <span>Helix Anchor Works</span></h2>
  <p class="welcome-text abs">Lorem ipsum dolor sit amet, consectetur adipiscing elit, sed do eiusmod tempor incididunt ut labore et dolore magna aliqua. Ut enim ad minim veniam, quis nostrud exercitation ullamco laboris nisi ut aliquip ex ea commodo consequat. Duis aute irure dolor in reprehenderit in voluptate velit esse cillum dolore eu</p>
  <div class="welcome-btn abs">READ MORE</div>
</section>

<section class="testimonials abs"></section>
<svg class="abs" style="left:104px;top:782px" width="26" height="66" viewBox="0 0 26 66"><polyline points="24,1 2,33 24,65" fill="none" stroke="#bbb" stroke-width="1.2"/></svg>
<svg class="abs" style="left:591px;top:782px" width="26" height="66" viewBox="0 0 26 66"><polyline points="2,1 24,33 2,65" fill="none" stroke="#bbb" stroke-width="1.2"/></svg>
<div class="quote-box abs"></div>
<svg class="abs" style="left:446px;top:784px" width="16" height="16" viewBox="0 0 16 16"><polygon points="0,0 16,0 0,16" fill="#fff"/></svg>
<svg class="quote-mark abs" width="28" height="22" viewBox="0 0 28 22" fill="#0a64d8"><circle cx="6.5" cy="15" r="6"/><path d="M1 14C1 7 4 2 10 0l1 2c-4 2-5 5-5 8z"/><circle cx="21" cy="15" r="6"/><path d="M15.5 14c0-7 3-12 9-14l1 2c-4 2-5 5-5 8z"/></svg>
<p class="quote-text abs">Lorem ipsum dolor sit amet, consectetur adipiscing elit, sed do eiusmod tempor incididunt ut labore et dolore magna aliqua. Ut enim ad minim veniam, quis nostrud exercitation ullamco laboris nisi ut aliquip ex ea commodo consequat.</p>
<div class="avatar abs" role="img" aria-label="Portrait photo of the client giving the testimonial"></div>
<div class="person abs">Dana Whitfield</div>
<div class="person-loc abs">City&nbsp; Location</div>

<footer class="footer abs" role="img" aria-label="Dark faded road map in the background"></footer>
<h3 class="footer-h contact-h abs">Contact Us</h3>
<div class="contact-lines abs">CALL TOLL-FREE<br>1-800-555-218<br>No.5&nbsp; Address Line1<br>Address Line-2&nbsp; 123450</div>
<div class="social abs"><span class="on"></span><span></span><span></span></div>
<div class="divider abs"></div>
<h3 class="footer-h news-h abs">News Letter&nbsp; Signup</h3>
<p class="news-text abs">Lorem ipsum dolor sit amet, consectetur adipiscing elitsed do eiusmod tempor incididunt</p>
<div class="email abs">Email Address</div>
<div class="subscribe abs">SUBSCRIBE</div>

<div class="bottom-bar abs"></div>
<div class="legal abs">Policies&nbsp; |&nbsp; Privacy&nbsp; |&nbsp; Terms &amp; Conditions</div>
<div class="copyright abs">Copyright 2015 Comapny name. All Rights Reserved.</div>

</body>
</html>
```